Business Card Design & Logo Design

Im a new company selling: balloons, bespoke gift wrapping services & Christmas decorating services i.e. I will come and decorate your tree, wrap your xmas presents, set & decorate your dining table, help you host your xmas party etc. etc.

I don't do 'cheesey' stuff so need a sophisticated card.

I love b&w colours, I love stripes and smart looking stuff.

I do already have an idea and if I don't find anything else then I will go with my idea but would then just need somebody to create the artwork for me.

www.copperwillow.co.uk is currently in the process of being designed so any ideas of logos/designs must also work with a website.

Industry/Entity Type

Business

Contact Information for Business Card

Copper Willow
Ashcombe Vale
KT14 9RD
Thornleighshire
01632 960418
or
07700 900736

treats@copperwillow.co.uk

```html
<!DOCTYPE html>
<html lang="en">
<head>
<meta charset="utf-8">
<title>Copper Willow – Business Cards</title>
<link rel="stylesheet" href="https://fonts.googleapis.com/css2?family=Lato:wght@300;400&display=swap">
<style>
  :root {
    --page-bg: #e9e9e9;
    --card-base: #121212;
    --card-sheen: rgba(255, 255, 255, 0.07);
    --text-light: #e6e6e6;
    --text-muted: #6f6f6f;
    --accent-orange: #f7941d;
    --accent-blue: #1ba1e2;
  }
  * { box-sizing: border-box; margin: 0; padding: 0; }
  html, body {
    width: 1200px;
    height: 900px;
    overflow: hidden;
    background: var(--page-bg);
    font-family: "Lato", sans-serif;
  }
  .canvas {
    position: relative;
    width: 1200px;
    height: 900px;
  }
  .card {
    position: absolute;
    width: 560px;
    height: 340px;
    background: var(--card-base);
    border-radius: 4px;
    overflow: hidden;
    box-shadow: 0 10px 28px rgba(0, 0, 0, 0.25);
  }
  .card-back { left: 60px; top: 100px; }
  .card-front { left: 580px; top: 470px; }
  .card-sheen {
    position: absolute;
    inset: 0;
    width: 100%;
    height: 100%;
  }
  .card-content {
    position: relative;
    width: 100%;
    height: 100%;
  }

  /* Back card */
  .back-brand {
    position: absolute;
    left: 40px;
    top: 152px;
    display: flex;
    align-items: center;
    gap: 10px;
  }
  .brand-dot {
    width: 14px;
    height: 14px;
    border-radius: 50%;
    background: var(--accent-orange);
  }
  .back-brand .brand-name {
    font-weight: 400;
    font-size: 22px;
    color: var(--accent-orange);
    letter-spacing: 0.5px;
    white-space: nowrap;
  }
  .contact-list {
    position: absolute;
    left: 262px;
    top: 96px;
    list-style: none;
    color: var(--text-light);
    font-weight: 300;
    font-size: 17px;
    line-height: 1.15;
  }
  .contact-item {
    display: flex;
    align-items: flex-start;
    gap: 12px;
    margin-bottom: 14px;
    white-space: nowrap;
  }
  .contact-icon {
    flex: 0 0 16px;
    width: 16px;
    height: 16px;
    margin-top: 2px;
  }

  /* Front card */
  .front-brand {
    position: absolute;
    left: 0;
    right: 0;
    top: 120px;
    display: flex;
    justify-content: center;
    align-items: center;
    gap: 14px;
  }
  .front-brand .brand-dot { width: 18px; height: 18px; }
  .front-brand .brand-name {
    font-weight: 400;
    font-size: 50px;
    color: var(--text-light);
    letter-spacing: 1px;
    white-space: nowrap;
  }
  .tagline {
    position: absolute;
    right: 90px;
    top: 200px;
    font-weight: 300;
    font-size: 22px;
    letter-spacing: 2px;
    color: var(--text-muted);
  }
</style>
</head>
<body>
<main class="canvas">

  <section class="card card-back" aria-label="Business card, contact side">
    <svg class="card-sheen" viewBox="0 0 560 340" preserveAspectRatio="none" aria-hidden="true">
      <ellipse cx="90" cy="330" rx="330" ry="250" fill="var(--card-sheen)"/>
      <ellipse cx="520" cy="150" rx="170" ry="260" fill="var(--card-sheen)"/>
    </svg>
    <div class="card-content">
      <div class="back-brand">
        <span class="brand-dot"></span>
        <span class="brand-name">Copper Willow</span>
      </div>
      <ul class="contact-list">
        <li class="contact-item">
          <svg class="contact-icon" viewBox="0 0 16 16" aria-hidden="true">
            <path d="M8 1a5 5 0 0 0-5 5c0 3.6 5 9 5 9s5-5.4 5-9a5 5 0 0 0-5-5zm0 7a2 2 0 1 1 0-4 2 2 0 0 1 0 4z" fill="var(--accent-blue)"/>
          </svg>
          <span>Ashcombe Vale KT14 9RD<br>Thornleighshire</span>
        </li>
        <li class="contact-item">
          <svg class="contact-icon" viewBox="0 0 16 16" aria-hidden="true">
            <path d="M4 1.5l2.2 3-1.4 1.6c.8 1.8 2.3 3.3 4.1 4.1l1.6-1.4 3 2.2-1.3 2.6C7 13.6 2.4 9 2 3l2-1.5z" fill="var(--accent-blue)"/>
          </svg>
          <span>01632 960418 or 07700 900736</span>
        </li>
        <li class="contact-item">
          <svg class="contact-icon" viewBox="0 0 16 16" aria-hidden="true">
            <rect x="1" y="3.5" width="14" height="10" fill="var(--accent-blue)"/>
            <path d="M1 3.5l7 5.5 7-5.5" fill="none" stroke="var(--card-base)" stroke-width="1.2"/>
          </svg>
          <span>treats@copperwillow.co.uk</span>
        </li>
      </ul>
    </div>
  </section>

  <section class="card card-front" aria-label="Business card, brand side">
    <svg class="card-sheen" viewBox="0 0 560 340" preserveAspectRatio="none" aria-hidden="true">
      <ellipse cx="110" cy="330" rx="320" ry="260" fill="var(--card-sheen)"/>
      <ellipse cx="530" cy="160" rx="160" ry="260" fill="var(--card-sheen)"/>
    </svg>
    <div class="card-content">
      <div class="front-brand">
        <span class="brand-dot"></span>
        <span class="brand-name">Copper Willow</span>
      </div>
      <p class="tagline">DECORATION</p>
    </div>
  </section>

</main>
</body>
</html>
```